当社は、神戸で埋蔵文化財発掘調査を行う会社として営業しております。
この業界では、全国的に有名ではあるのですが、この度、新たな顧客獲得の一つのアイテムとしてDMを検討しております。
一般的にそんな仕事が存在している事の認識が低く、シンプルでインパクトの強いDMのデザインの作成をお願いします。

①DMデザインの作成(B5サイズ)
②表面 当社ロゴ、住所、TEL、FAX、URL
③裏面 シンプルでインパクトのあるもの

埋蔵文化財発掘調査について詳しく無い方も沢山おられると思いますので、
当社HP http://www.tamurakensa.com/ で確認してください。

イラストレーター形式
PDF形式
質疑回答を元に、裏面を尚且つシンプルで埋蔵文化財発掘調査をインパクトあるデザインをお願いします。
尚、ハガキとして郵送の予定です。

シンプルかつインパクトのあるデザインで、受け取り手にも会社の内容が伝わりやすいと思い採用させて頂きました。

たくさんのご提案頂きまして、誠にありがとうございます。
選考中も非常に悩むデザインが多く、選考に時間が掛かってしまいました。
本当にありがとうございました。

```html
<!DOCTYPE html>
<html lang="ja">
<head>
<meta charset="utf-8">
<title>田村建産株式会社 DM</title>
<link href="https://fonts.googleapis.com/css2?family=Noto+Serif+JP:wght@500;700;900&family=Noto+Sans+JP:wght@400;500;700&display=swap" rel="stylesheet">
<style>
:root{
  --paper:#ffffff;
  --sand:#efe9d6;
  --sand-line:#d9cfae;
  --stone-1:#9fb3ad;
  --stone-2:#6f8d88;
  --stone-3:#c9c3a6;
  --navy:#14265c;
  --green:#2f7a4a;
  --green-dark:#2d4f3a;
  --ink:#2b2b2b;
}
*{margin:0;padding:0;box-sizing:border-box}
html,body{width:851px;height:1200px;overflow:hidden;background:var(--paper)}
.card{position:relative;width:851px;height:1200px;background:var(--paper);font-family:"Noto Sans JP",sans-serif;color:var(--ink)}
.visual{position:absolute;left:0;top:672px;width:851px;height:370px}
.visual svg{position:absolute;inset:0}
.message{position:absolute;left:218px;top:818px;width:620px;font-family:"Noto Serif JP",serif;font-weight:900;color:var(--navy);font-size:30px;line-height:56px;white-space:nowrap;
  text-shadow:0 0 3px #fff,0 0 3px #fff,0 0 6px #fff,0 0 10px #fff}
.message em{font-style:normal;font-size:40px}
.business{position:absolute;left:213px;top:990px;display:flex;align-items:center;gap:8px;white-space:nowrap}
.business .label{background:var(--green);color:#fff;font-weight:700;font-size:12px;padding:2px 10px;border-radius:10px}
.business .items{font-weight:700;font-size:15px;color:var(--navy);text-shadow:0 0 3px #fff,0 0 5px #fff}
.business .items small{font-size:12px;font-weight:500}
.footer{position:absolute;left:0;top:1030px;width:851px;height:170px;background:var(--sand)}
.brand{position:absolute;left:34px;top:28px;display:flex;align-items:center;gap:6px}
.brand .mark{width:22px;height:22px;background:var(--green)}
.brand .name{font-weight:700;font-size:18px;color:var(--green);letter-spacing:1px}
.company{position:absolute;left:170px;top:6px;white-space:nowrap}
.company .tag{font-size:13px;font-weight:500;color:var(--green-dark)}
.company .title{font-family:"Noto Serif JP",serif;font-weight:700;font-size:38px;color:var(--green-dark);letter-spacing:3px;line-height:1.15}
.hq{position:absolute;left:34px;top:92px;font-size:12px;font-weight:500;white-space:nowrap}
.contact{position:absolute;left:574px;top:10px;font-weight:700;color:var(--green-dark);white-space:nowrap}
.contact div{display:flex;align-items:center;gap:8px;font-size:21px;line-height:33px}
.contact .url{font-size:15px;line-height:24px}
.contact .ico{width:24px;height:15px;background:var(--green);color:#fff;font-size:9px;display:flex;align-items:center;justify-content:center;border-radius:3px}
.branches{position:absolute;left:34px;top:114px;right:24px;border-top:1px solid var(--sand-line);padding-top:5px;display:grid;grid-template-columns:repeat(3,1fr);column-gap:14px;font-size:9.5px;line-height:12px;white-space:nowrap}
.branches b{display:inline-block;width:62px;font-weight:700}
</style>
</head>
<body>
<div class="card">
  <div class="visual" role="img" aria-label="発掘現場の土層と出土した古代の遺物の写真">
    <svg width="851" height="370" viewBox="0 0 851 370">
      <defs>
        <linearGradient id="site" x1="0" y1="0" x2="1" y2="1">
          <stop offset="0" stop-color="var(--stone-1)"/>
          <stop offset=".5" stop-color="var(--stone-2)"/>
          <stop offset="1" stop-color="var(--stone-3)"/>
        </linearGradient>
      </defs>
      <path d="M0 40 Q 420 -15 851 30 L851 370 L0 370 Z" fill="url(#site)"/>
    </svg>
  </div>
  <p class="message">私たちは、古来よりの<em>先人</em>がまもり<br>深い存在感と輝きをもつ<em>遺跡</em>を<br>感謝の気持ちと共に<em>未来</em>に伝えます。</p>
  <div class="business"><span class="label">事業内容</span><span class="items">埋蔵文化財発掘調査業務<small>／土木・建築工事／解体工事／運送</small></span></div>

  <div class="footer">
    <div class="brand"><span class="mark"></span><span class="name">TAMURA</span></div>
    <div class="company">
      <div class="tag">埋蔵文化財発掘調査業務・土木工事・建築工事</div>
      <div class="title">田村建産株式会社</div>
    </div>
    <div class="contact">
      <div><span class="ico">TEL</span>078-000-4410</div>
      <div><span class="ico">FAX</span>078-000-4416</div>
      <div class="url">http://www.tamurakensa.com/</div>
    </div>
    <div class="hq">本 社 〒651-0000 兵庫県神戸市西区北野台1丁目2番3号</div>
    <div class="branches">
      <div><b>大阪支店</b>大阪府大阪市北区中町1-2-3</div>
      <div><b>四国支店</b>香川県高松市南町4-5-6</div>
      <div><b>名古屋事務所</b>愛知県名古屋市東区1-1</div>
      <div><b>奈良支店</b>奈良県奈良市西町2-3-4</div>
      <div><b>小野支店</b>兵庫県小野市本町5-6</div>
      <div><b>和歌山営業所</b>和歌山県和歌山市3-2</div>
      <div><b>岡山支店</b>岡山県岡山市北区8-9</div>
      <div><b>伊丹支店</b>兵庫県伊丹市東町7-8</div>
      <div><b>鳥取支店</b>鳥取県鳥取市栄町4-1</div>
      <div><b>三重支店</b>三重県津市中央町2-4</div>
      <div><b>姫路支店</b>兵庫県姫路市南町3-5</div>
      <div><b>福岡支店</b>福岡県福岡市博多区6-2</div>
    </div>
  </div>
</div>
</body>
</html>
```